We are looking for Facebook and Instagram templates. To use both platforms we will use square images. We need a template for our posts, not the header image.
Most posts contain multiple images and we need a designoverlay in which we can embed our images.
Attached a screenshot of our website www.velutra.be, our logo in svg and ai. The monkey is our mascotte (excact this monkey, not another).
We offer teambuildings, the style should be fun. Colors are antracite, limegreen and white. I did attache the current layout for posts but we are not happy with this.
If we could have some small design elements (like stickers) we can always create a new layout but is feels the same.
Our website is quite simple, this should also be in these post designs. Simple forms, rounded corners.
Updates

Allow more time for the designers, good work requires more time

Target Market(s)

Teambuilding

Industry/Entity Type

Teambuilding

Other font styles liked:
• RobotoSlab

Requirements
Must have
• If we could have some small design elements (like stickers) we can always create a new layout but is feels the same.
Should not have
• Complex design, simple images works best for us

```html
<!DOCTYPE html>
<html lang="en">
<head>
<meta charset="utf-8">
<title>Velutra Het Anker – Team Building Post Templates</title>
<link rel="stylesheet" href="https://fonts.googleapis.com/css2?family=Londrina+Solid:wght@400;900&display=swap">
<style>
  :root {
    --antracite: #4a4a4b;
    --antracite-dark: #3a3a3b;
    --lime: #a8c424;
    --white: #ffffff;
    --ink: #2b2b2b;
    --photo-warm: #b07a3c;
    --photo-dark: #3b2c22;
  }
  * { box-sizing: border-box; margin: 0; padding: 0; }
  html, body { width: 1200px; height: 3599px; overflow: hidden; background: var(--antracite); }
  body { font-family: "Londrina Solid", "Arial Narrow", sans-serif; }

  .canvas { position: relative; width: 1200px; height: 3599px; overflow: hidden; }

  .post { position: absolute; left: 0; width: 1200px; height: 1200px; overflow: hidden; background: var(--antracite); }
  .post--quote { top: 0; }
  .post--single { top: 1200px; border-top: 1px solid var(--antracite-dark); }
  .post--grid { top: 2400px; height: 1199px; border-top: 1px solid var(--antracite-dark); }

  .splash { position: absolute; background: var(--lime); border-radius: 28px; }

  /* Quote post */
  .quote-panel {
    position: absolute; left: 80px; top: 226px; width: 1036px; height: 898px;
    background: var(--lime); transform: rotate(-1.5deg); border-radius: 10px;
  }
  .quote-text {
    position: absolute; left: 150px; top: 230px; width: 900px;
    text-align: center; font-weight: 400; font-size: 120px; line-height: 151px;
    color: var(--ink); text-transform: uppercase; letter-spacing: -1px;
    white-space: nowrap;
  }
  .quote-text .light { color: var(--white); }

  .tag {
    position: absolute; background: var(--lime); color: var(--ink);
    font-weight: 400; text-transform: uppercase; transform: rotate(-2deg);
    border-radius: 8px; display: flex; align-items: center;
    white-space: nowrap; overflow: hidden;
  }
  .tag--welcome { left: 78px; top: 66px; width: 566px; height: 136px; font-size: 104px; padding-left: 72px; }
  .tag--section { left: 62px; top: 54px; width: 582px; height: 140px; font-size: 92px; padding-left: 30px; z-index: 3; }

  .mascot {
    position: absolute; border-radius: 46% 54% 40% 60% / 55% 45% 55% 45%;
  }
  .mascot--white { background: var(--white); }
  .mascot--lime { background: var(--lime); }

  /* Name lockup */
  .brand {
    position: absolute; left: 480px; width: 240px; height: 84px;
    border: 3px solid #d8d8d8; background: var(--antracite);
    color: var(--white); text-align: center; text-transform: uppercase; z-index: 4;
  }
  .brand__name { display: block; font-weight: 400; font-size: 40px; line-height: 44px; margin-top: 4px; letter-spacing: 2px; }
  .brand__place { display: block; font-weight: 400; font-size: 24px; line-height: 28px; border-top: 3px solid #d8d8d8; letter-spacing: 3px; }
  .post--quote .brand { top: 1083px; }
  .post--single .brand, .post--grid .brand { top: 1090px; }

  /* Photo frames */
  .frame { position: absolute; background: var(--white); border-radius: 6px; }
  .photo {
    position: absolute; border-radius: 4px;
    background: linear-gradient(160deg, var(--photo-warm) 0%, #8a6a4c 45%, var(--photo-dark) 100%);
  }
  .frame--large { left: 78px; top: 94px; width: 1034px; height: 1032px; transform: rotate(-2deg); }
  .frame--large .photo { left: 34px; top: 40px; width: 952px; height: 952px; }

  .frame--tl { left: 84px; top: 172px; width: 490px; height: 434px; transform: rotate(-2deg); }
  .frame--tr { left: 580px; top: 118px; width: 482px; height: 434px; transform: rotate(-3deg); }
  .frame--bl { left: 112px; top: 628px; width: 504px; height: 452px; transform: rotate(-2deg); }
  .frame--br { left: 630px; top: 594px; width: 488px; height: 460px; transform: rotate(-3deg); }
  .frame--small .photo { left: 24px; top: 26px; right: 24px; bottom: 26px; }

  .badge-circle {
    position: absolute; left: 524px; top: 580px; width: 176px; height: 176px;
    border-radius: 50%; background: var(--lime); z-index: 3;
  }
  .badge-circle .mascot { left: 34px; top: 44px; width: 108px; height: 88px; }
</style>
</head>
<body>
<main class="canvas">

  <section class="post post--quote">
    <div class="splash" style="left:-40px;top:760px;width:220px;height:220px;transform:rotate(20deg)"></div>
    <div class="splash" style="left:1060px;top:150px;width:200px;height:260px;transform:rotate(-15deg)"></div>
    <div class="quote-panel"></div>
    <div class="tag tag--welcome">Welcome</div>
    <p class="quote-text">
      <span class="light">Great teams</span><br>
      Don't just work<br>
      together<br>
      they <span class="light">have fun</span><br>
      <span class="light">together</span>
    </p>
    <div class="mascot mascot--white" role="img" aria-label="Monkey mascot silhouette in white" style="left:832px;top:872px;width:286px;height:250px"></div>
    <div class="brand"><span class="brand__name">Velutra</span><span class="brand__place">Het Anker</span></div>
  </section>

  <section class="post post--single">
    <div class="splash" style="left:-60px;top:560px;width:200px;height:300px;transform:rotate(14deg)"></div>
    <div class="splash" style="left:1080px;top:90px;width:180px;height:280px;transform:rotate(-12deg)"></div>
    <div class="tag tag--section">Team building</div>
    <div class="frame frame--large">
      <div class="photo" role="img" aria-label="Photo slot: team gathered at a bar with hanging bulb lights"></div>
    </div>
    <div class="mascot mascot--lime" role="img" aria-label="Monkey mascot silhouette in lime green" style="left:818px;top:812px;width:286px;height:278px;z-index:2"></div>
    <div class="brand"><span class="brand__name">Velutra</span><span class="brand__place">Het Anker</span></div>
  </section>

  <section class="post post--grid">
    <div class="splash" style="left:-70px;top:820px;width:210px;height:300px;transform:rotate(18deg)"></div>
    <div class="splash" style="left:1070px;top:80px;width:190px;height:300px;transform:rotate(-10deg)"></div>
    <div class="tag tag--section">Team building</div>
    <div class="frame frame--small frame--tl"><div class="photo" role="img" aria-label="Photo slot 1: team at the bar"></div></div>
    <div class="frame frame--small frame--tr"><div class="photo" role="img" aria-label="Photo slot 2: team at the bar"></div></div>
    <div class="frame frame--small frame--bl"><div class="photo" role="img" aria-label="Photo slot 3: team at the bar"></div></div>
    <div class="frame frame--small frame--br"><div class="photo" role="img" aria-label="Photo slot 4: team at the bar"></div></div>
    <div class="badge-circle">
      <div class="mascot mascot--white" role="img" aria-label="Monkey mascot silhouette in white"></div>
    </div>
    <div class="brand"><span class="brand__name">Velutra</span><span class="brand__place">Het Anker</span></div>
  </section>

</main>
</body>
</html>
```